Physiotherapist for Horse and Rider

I need a web design and a working, functioning website for my profession as physiotherapist. Tabs available for the therapy I offer such a massage, stretching, taping, elektrotherapie en advies. Another tab for introducing myself and one for workshops I want to give. I like a tab for photo's and one for how the clients can contact me.

I like it similar too velnor.be Not too much text to read, a beautifull design with matching colours and nice photo's.

Target Market(s)

horse people

Industry/Entity Type

Massage

Number of Pages Required

1 page

Font styles to use
Serif
Script

Colors
34a6d7
0355a3
0493ce

Requirements
Must have
• I like the blue colours from my logo design.
• Contact with e-mail.
• domain name Brivo Lumé
Nice to have
• some off the photo's I uploaded

```html
<!DOCTYPE html>
<html lang="en">
<head>
<meta charset="utf-8">
<title>Brivo Lumé – Physiotherapist for Horse and Rider</title>
<link href="https://fonts.googleapis.com/css2?family=Open+Sans:wght@400;600&family=Roboto+Condensed:wght@400;700&display=swap" rel="stylesheet">
<style>
:root{
  --blue:#0493ce;
  --blue-light:#34a6d7;
  --blue-deep:#0355a3;
  --ink:#222;
  --muted:#666;
  --grey-bg:#f0f0f0;
  --footer:#141414;
  --footer-bottom:#050505;
  --white:#fff;
}
*{box-sizing:border-box;margin:0;padding:0}
html,body{width:1200px;height:3035px;overflow:hidden}
body{font-family:"Open Sans",Arial,sans-serif;color:var(--ink);background:var(--white);position:relative}
.abs{position:absolute}

/* header */
.site-header{position:absolute;left:0;top:0;width:1200px;height:126px;background:var(--white)}
.topbar{position:absolute;left:370px;top:0;width:830px;height:30px;background:var(--blue-deep);clip-path:polygon(0 0,100% 0,100% 100%,30px 100%)}
.topbar .contact{position:absolute;left:52px;top:6px;font-size:13px;color:var(--white);display:flex;gap:30px}
.topbar .tools{position:absolute;right:40px;top:8px;display:flex;gap:6px;align-items:center}
.topbar .sq{width:13px;height:13px;background:var(--white);border-radius:2px}
.topbar .search{margin-right:26px}
.brand{position:absolute;left:82px;top:12px;width:170px;text-align:center}
.brand .mark{width:34px;height:34px;border-radius:50%;background:var(--blue-deep);margin:0 auto 6px}
.brand .name{font-size:27px;color:var(--blue-deep);letter-spacing:1px;line-height:1}
.brand .person{font-size:14px;color:var(--blue-deep);margin-top:3px}
.brand .tag{font-size:8px;color:var(--blue-deep)}
.main-nav{position:absolute;left:368px;top:77px;display:flex;gap:20px;font-size:13.5px;text-transform:uppercase;color:#333}
.main-nav .active{color:var(--blue);border-bottom:2px solid var(--blue);padding-bottom:5px}

/* hero */
.hero{position:absolute;left:0;top:126px;width:1200px;height:552px;background:linear-gradient(90deg,#6e5a45 0%,#8b6a4a 35%,#4a8fb0 55%,#5a4634 75%,#3a3a3a 100%)}
.hero h1{position:absolute;left:86px;top:338px;font-family:"Roboto Condensed",Arial,sans-serif;font-weight:700;font-size:60px;color:var(--white)}
.hero p{position:absolute;left:86px;top:408px;font-family:"Roboto Condensed",Arial,sans-serif;font-size:27px;color:var(--white)}
.hero .arrow{position:absolute;top:474px;width:28px;height:28px;border-radius:50%;background:#111}
.hero .arrow svg{position:absolute;left:8px;top:7px}

/* generic section titles */
.section-title{position:absolute;left:0;width:1200px;text-align:center;font-size:28px;font-weight:400;text-transform:uppercase;color:var(--ink)}

/* treatments */
.treatments{position:absolute;left:0;top:678px;width:1200px;height:559px}
.treatments .lead{position:absolute;top:112px;width:1200px;text-align:center;font-size:14px;color:#555}
.treatment{position:absolute;top:186px;width:200px;text-align:center}
.treatment .ring{width:164px;height:164px;margin:0 auto;border-radius:50%;background:#fafafa;border:1px solid #e4e4e4;box-shadow:inset 0 0 18px rgba(0,0,0,.08);display:flex;align-items:center;justify-content:center}
.treatment .icon{width:80px;height:80px;border-radius:50%;background:var(--blue)}
.treatment h3{margin-top:32px;font-size:18px;font-weight:400;text-transform:uppercase;letter-spacing:.5px}
.treatment p{margin-top:8px;font-size:13px;line-height:20px;color:var(--muted);height:40px;overflow:hidden}
.treatment a{display:block;margin-top:10px;font-size:13px;color:var(--blue);text-decoration:none}

/* about */
.about{position:absolute;left:0;top:1237px;width:1200px;height:344px;background:linear-gradient(90deg,#1d67b4,var(--blue-deep) 40%,#0a5fb2)}
.about .section-title{color:var(--white);top:70px}
.about p{position:absolute;left:148px;top:120px;width:904px;text-align:center;font-size:13.5px;line-height:26px;color:var(--white)}
.about .btn{position:absolute;left:540px;top:243px;width:120px;height:34px;border-radius:17px;background:var(--white);color:#222;font-size:13px;text-transform:uppercase;display:flex;align-items:center;justify-content:center}

/* workshops */
.workshops{position:absolute;left:0;top:1581px;width:1200px;height:541px}
.workshops .section-title{top:74px}
.workshop{position:absolute;top:151px;width:478px;text-align:center}
.workshop .photo{height:246px}
.workshop h3{margin-top:18px;font-size:20px;font-weight:400}
.workshop time{display:block;margin-top:10px;font-size:14px;color:#444}

/* blog */
.blog{position:absolute;left:0;top:2122px;width:1200px;height:443px;background:var(--grey-bg)}
.blog .section-title{top:54px}
.post{position:absolute;top:123px;width:311px;text-align:center}
.post .photo{height:193px}
.post h3{margin-top:16px;font-size:16px;font-weight:400}
.post time{display:block;margin-top:2px;font-size:13px;color:#333}

/* partners */
.partners{position:absolute;left:0;top:2565px;width:1200px;height:170px;display:flex;justify-content:center;align-items:center;gap:52px}
.partners .badge{width:130px;height:34px;background:#c9c9c9;border-radius:4px}

/* footer */
.site-footer{position:absolute;left:0;top:2735px;width:1200px;height:218px;background:var(--footer);color:var(--white)}
.site-footer .brand{top:40px;left:92px;width:180px}
.site-footer .brand .mark{background:var(--white)}
.site-footer .brand .name,.site-footer .brand .person,.site-footer .brand .tag{color:var(--white)}
.footer-col{position:absolute;top:46px;font-size:12px;line-height:25px}
.footer-col h4{font-size:15px;font-weight:400;text-transform:uppercase;margin-bottom:14px;line-height:1}
.footer-col ul{list-style:none}
.footer-col li::before{content:"";display:inline-block;border-left:5px solid var(--white);border-top:4px solid transparent;border-bottom:4px solid transparent;margin-right:9px}
.newsletter p{width:210px;line-height:18px}
.newsletter form{display:flex;margin-top:18px}
.newsletter .field{width:146px;height:30px;background:var(--white);color:#777;font-size:12px;padding:7px 10px}
.newsletter .submit{width:56px;height:30px;background:var(--blue-deep);font-size:12px;display:flex;align-items:center;justify-content:center}
.copyright{position:absolute;left:0;top:2953px;width:1200px;height:82px;background:var(--footer-bottom);color:var(--white)}
.copyright p{position:absolute;left:88px;top:31px;font-size:14px}
.copyright .social{position:absolute;left:976px;top:28px;display:flex;gap:10px}
.copyright .social span{width:26px;height:26px;border-radius:3px}
</style>
</head>
<body>

<header class="site-header">
  <div class="topbar">
    <div class="contact"><span>&#9990; : +32-9-4417203</span><span>&#9993; : info@velnor.be</span></div>
    <div class="tools">
      <svg class="search" width="14" height="14" viewBox="0 0 14 14"><circle cx="6" cy="6" r="4.5" fill="none" stroke="#fff" stroke-width="2"/><line x1="9.5" y1="9.5" x2="13" y2="13" stroke="#fff" stroke-width="2"/></svg>
      <span class="sq"></span><span class="sq"></span><span class="sq"></span><span class="sq"></span>
    </div>
  </div>
  <div class="brand">
    <div class="mark"></div>
    <div class="name">BRIVO LUMÉ</div>
    <div class="person">Marthe Delcourt</div>
    <div class="tag">Kinesitherapeut voor paard en ruiter</div>
  </div>
  <nav class="main-nav">
    <span class="active">Home</span><span>About us</span><span>Massage</span><span>Stretching</span><span>Taping</span><span>Elektrotherapie en advies</span><span>Photos</span><span>Contact us</span>
  </nav>
</header>

<section class="hero" role="img" aria-label="Photo of the physiotherapist treating a brown horse in a stable">
  <h1>PHYSIOTHERAPIST</h1>
  <p>Who does for Horse and Rider</p>
  <span class="arrow" style="left:1046px"><svg width="12" height="14" viewBox="0 0 12 14"><path d="M8 2 3 7l5 5" fill="none" stroke="#fff" stroke-width="2"/></svg></span>
  <span class="arrow" style="left:1078px"><svg width="12" height="14" viewBox="0 0 12 14"><path d="M4 2l5 5-5 5" fill="none" stroke="#fff" stroke-width="2"/></svg></span>
</section>

<section class="treatments">
  <h2 class="section-title" style="top:60px">Treatments</h2>
  <p class="lead">Neque porro quisquam est qui dolorem ipsum quia dolor sit amet, consectetur</p>
  <div class="treatment" style="left:100px"><div class="ring"><div class="icon" role="img" aria-label="Horse illustration for massage"></div></div><h3>Massage</h3><p>As a physiotherapist I go looking for the cause of the problem.</p><a>Read More -&gt;</a></div>
  <div class="treatment" style="left:370px"><div class="ring"><div class="icon" role="img" aria-label="Horse illustration for stretching"></div></div><h3>Stretching</h3><p>These shouldsymptoms are treated first, so that the underlying</p><a>Read More -&gt;</a></div>
  <div class="treatment" style="left:640px"><div class="ring"><div class="icon" role="img" aria-label="Horse and rider illustration for taping"></div></div><h3>Taping</h3><p>As a physiotherapist I go looking for the cause of the problem.</p><a>Read More -&gt;</a></div>
  <div class="treatment" style="left:910px"><div class="ring"><div class="icon" role="img" aria-label="Horse head illustration for elektrotherapie"></div></div><h3>Elektrotherapie</h3><p>These shouldsymptoms are treated first, so that the underlying</p><a>Read More -&gt;</a></div>
</section>

<section class="about">
  <h2 class="section-title">About us</h2>
  <p>Marthe Delcourt, 32 years, Brivo Lumé. Marthe graduated from the University of Westvaal as Human physiotherapist in 2007. She immediately began training Dierfysiotherapie in Faculty of Veterinary Medicine, Oostmeer and graduated as a physiotherapist for horses in 2010. She combines both the Physiotherapist for Horse and Rider. From year to year they schooled themselves in in Human Manual Therapy. In year she learned natural hoof trimming. Since 2016 she has also engrossed in the Manual Taping Concept and Hoefband Taping.</p>
  <span class="btn">Read more</span>
</section>

<section class="workshops">
  <h2 class="section-title">Workshops</h2>
  <article class="workshop" style="left:103px"><div class="photo" role="img" aria-label="Photo of a woman massaging a dark horse" style="background:linear-gradient(90deg,#8a8c86,#4b4a44 60%,#2d2a26)"></div><h3>Self massaging your horse</h3><time>19/05/17</time></article>
  <article class="workshop" style="left:625px"><div class="photo" role="img" aria-label="Photo of a woman treating a brown horse in a barn" style="background:linear-gradient(90deg,#6f6b63,#7b5638 45%,#b9c4c9 80%,#d6d6d0)"></div><h3>Wellness weekend for horse and rider</h3><time>17/05/17</time></article>
</section>

<section class="blog">
  <h2 class="section-title">Latest Blog</h2>
  <article class="post" style="left:97px"><div class="photo" role="img" aria-label="Photo of a woman beside a dark horse" style="background:linear-gradient(90deg,#3f3a34,#5f5a52 55%,#8d8a83)"></div><h3>Neque porro quisquam est qui</h3><time>19/05/16</time></article>
  <article class="post" style="left:449px"><div class="photo" role="img" aria-label="Photo of a horse leg being treated" style="background:linear-gradient(90deg,#a8a6a0,#7d5536 50%,#c8c8c2)"></div><h3>Dolorem ipsum quia dolor sit amet</h3><time>17/05/16</time></article>
  <article class="post" style="left:800px"><div class="photo" role="img" aria-label="Photo of a woman with a dark horse in a stable" style="background:linear-gradient(90deg,#55514b,#3b3832 60%,#2a2723)"></div><h3>Quisquam est qui dolorem</h3><time>13/05/16</time></article>
</section>

<section class="partners" aria-label="Partners">
  <span class="badge"></span><span class="badge"></span><span class="badge"></span><span class="badge"></span><span class="badge"></span><span class="badge"></span>
</section>

<footer class="site-footer">
  <div class="brand">
    <div class="mark"></div>
    <div class="name">BRIVO LUMÉ</div>
    <div class="person">Marthe Delcourt</div>
    <div class="tag">Kinesitherapeut voor paard en ruiter</div>
  </div>
  <div class="footer-col" style="left:378px"><h4>Links</h4><ul><li>About us</li><li>Massage</li><li>Stretching</li><li>Taping</li></ul></div>
  <div class="footer-col" style="left:580px"><h4>Get in touch</h4><p>Address : 12 Hoefstraat, Weidekant<br>9050</p><p style="margin-top:6px">Phone : (09)226-7814</p><p style="margin-top:6px">Email : info@velnor.be</p></div>
  <div class="footer-col newsletter" style="left:905px"><h4>Newsletter</h4><p>Your about us information would fit here nicely.</p><form><span class="field">Email address</span><span class="submit">Submit</span></form></div>
</footer>

<div class="copyright">
  <p>Copyright © 2017. All Rights Reserved</p>
  <div class="social"><span style="background:#1da1f2"></span><span style="background:#d62d20"></span><span style="background:#3b5998"></span><span style="background:#0e76a8"></span></div>
</div>

</body>
</html>
```